Harbinger Noble Alloys Works Business Cards

We are wanting to have a new business card designed for our company as we go to a convention. We want to balance business/Modern with elegance and beauty. Our company sells highend jewelry pieces. We want to utilize the colors of Black and Gold and have gold foiled fonts to be physically printed on the business cards.
We also would like to have space to write notes on the back side of the business card. When we meet people at jewelry conventions we would like to write notes if possible.
Here are websites and designs that we like the look and feel of these companies and you can use these as design ideas.
https://www.lorvanne.com
https://www.bellquist.com/en-us/home
Here is our company website link
www.harbingernaw.com
I also up loaded two versions of our logo.
- Update 4.26.22
I have uploaded photos of a business card we like. this card has raised embossed letters that you can feel. the raise letters are like a plastic but we don't need to use that...I uploaded to show you that we like the experience of the client feeling the characters of the logo. we also would like to have the material as a satin or some material very soft.
- Maybe we can get designs with beautiful gold foiling and raised characters and logos. we like simplicity...not busy but an elegant design. We need to write notes and would like a section where we can write notes. but we want an elegant style and the client has an experience with the feel of the card when they touch the card.
Colors
- Main colors Black & Gold
- white or light colors for small notes section.
Specialty ideals and things we would like to see based on your design styles.
- raised fonts
- raised logos
- gold foiling
- satin/soft finish on the card material.
we are wanting to design a business card that looks elegant and clean. When the client is handed the business card we want them to physically experience the business card as well by touching the raised logos or fonts and the base material is soft satin. I hope this helps with further designs.
thank you all
We uploaded a new contact layout that we have designed in our office. we would like to see how this would look on your designs.
thank you
I just finished uploading the Contact Layout. the colors are just examples. please use this layout as an idea and use colors based on the feed back we have given each of you personally.
Contact Information for Business Card
we need an area to write notes, we would like to have our logos or the diamond of our logo or the business card to have embossed sections to the business card so when the customer touches the card they can feel the logo. we would also like sections of our business card to have gold foiling. we would also like to use a satin soft paper with our card. when the client touches the card its super soft and high quality
Requirements
Must have
- we would like to have our logos or the diamond of our logo or the business card to have embossed sections to the business card so when the customer touches the card they can feel the logo. we would also like sections of our business card to have gold foiling. we would also like to use a satin soft paper with our card. when the client touches the card its super soft and high quality
Nice to have
- we would like to have our logos or the diamond of our logo or the business card to have embossed sections to the business card so when the customer touches the card they can feel the logo. we would also like sections of our business card to have gold foiling.

```html
<!DOCTYPE html>
<html lang="en">
<head>
<meta charset="utf-8">
<title>Harbinger Noble Alloys Works – Business Card</title>
<link rel="stylesheet" href="https://fonts.googleapis.com/css2?family=Roboto:wght@400;500&display=swap">
<style>
  :root {
    --backdrop: #c3c3c5;
    --ink: #201c1a;
    --ink-soft: #3a3633;
    --gold: #e7c14a;
    --gold-deep: #b97a2a;
    --gold-pale: #f7ea8e;
    --pearl: #f1ecec;
    --notes: #ebe6e5;
    --note-line: #c9954a;
  }
  * { margin: 0; padding: 0; box-sizing: border-box; }
  html, body {
    width: 1200px; height: 1013px; overflow: hidden;
    background: var(--backdrop);
  }
  .sheet { position: relative; width: 1200px; height: 1013px; }
  .card {
    position: absolute; top: 87px; width: 504px; height: 840px; display: block;
  }
  .card--front { left: 79px; }
  .card--back { left: 624px; }
  .brand-name { font-family: 'Roboto', sans-serif; font-weight: 500; font-size: 44px; letter-spacing: 1px; }
  .person-name { font-family: 'Roboto', sans-serif; font-weight: 500; font-size: 78px; letter-spacing: 3px; }
  .person-role { font-family: 'Roboto', sans-serif; font-weight: 400; font-size: 32px; letter-spacing: 9px; }
  .contact-text { font-family: 'Roboto', sans-serif; font-weight: 400; font-size: 32px; }
</style>
</head>
<body>
<main class="sheet">

  <!-- Front -->
  <svg class="card card--front" viewBox="0 0 878 1463" xmlns="http://www.w3.org/2000/svg" aria-label="Business card front">
    <defs>
      <linearGradient id="front-sky" x1="0" y1="0" x2="0" y2="1">
        <stop offset="0" stop-color="#c69741"/>
        <stop offset="0.35" stop-color="#f4e48a"/>
        <stop offset="1" stop-color="#f4e48a"/>
      </linearGradient>
      <linearGradient id="gold-sweep" x1="0" y1="0" x2="1" y2="0">
        <stop offset="0" stop-color="#e6bd45"/>
        <stop offset="0.45" stop-color="#f8ec95"/>
        <stop offset="1" stop-color="#e2b540"/>
      </linearGradient>
      <linearGradient id="gold-coin" x1="0" y1="0" x2="1" y2="0">
        <stop offset="0" stop-color="#f4e09a"/>
        <stop offset="1" stop-color="#b97a2a"/>
      </linearGradient>
      <linearGradient id="gold-arc" x1="0" y1="0" x2="1" y2="0">
        <stop offset="0" stop-color="#f1dc78"/>
        <stop offset="1" stop-color="#c0832e"/>
      </linearGradient>
      <linearGradient id="dome-dark" x1="0" y1="0" x2="0" y2="1">
        <stop offset="0" stop-color="#3a3633"/>
        <stop offset="1" stop-color="#1d1a18"/>
      </linearGradient>
      <linearGradient id="dash-gold" x1="0" y1="0" x2="1" y2="0">
        <stop offset="0" stop-color="#e9c44a"/>
        <stop offset="0.5" stop-color="#f7e27a"/>
        <stop offset="1" stop-color="#bf7f2c"/>
      </linearGradient>
    </defs>

    <rect class="front-sky" width="878" height="1463" fill="url(#front-sky)"/>
    <path class="wave wave--ink" d="M0,318 C150,255 300,468 439,468 S728,255 878,318 L878,1463 L0,1463 Z" fill="var(--ink)"/>
    <path class="wave wave--pearl" d="M0,350 C150,290 300,490 439,490 S728,290 878,350 L878,1463 L0,1463 Z" fill="var(--pearl)"/>
    <path class="wave wave--gold" d="M0,378 C150,320 300,505 439,505 S728,320 878,378 L878,1463 L0,1463 Z" fill="url(#gold-sweep)"/>
    <path class="wave wave--body" d="M0,413 C150,355 300,482 439,482 S728,355 878,413 L878,1463 L0,1463 Z" fill="var(--ink)"/>
    <circle class="medallion" cx="439" cy="420" r="47" fill="url(#gold-coin)" stroke="var(--ink)" stroke-width="12"/>

    <circle class="brand-mark" cx="439" cy="130" r="24" fill="var(--ink)"/>
    <text class="brand-name" x="439" y="222" text-anchor="middle" fill="var(--ink)">Harbinger Noble Alloys Works</text>

    <text class="person-name" x="439" y="663" text-anchor="middle" fill="var(--gold)">DELIA MARREN</text>
    <text class="person-role" x="439" y="721" text-anchor="middle" fill="var(--gold)">CEO &amp; FOUNDER</text>
    <line class="divider" x1="153" y1="788" x2="723" y2="788" stroke="url(#dash-gold)" stroke-width="5" stroke-dasharray="28 26"/>

    <g class="contact">
      <g class="contact-icon">
        <circle cx="232" cy="866" r="21" fill="url(#gold-coin)"/>
        <path d="M232,878 C224,868 222,864 222,860 A10,10 0 0 1 242,860 C242,864 240,868 232,878 Z" fill="var(--ink)"/>
        <circle cx="232" cy="860" r="4" fill="var(--gold)"/>
      </g>
      <text class="contact-text" x="265" y="870" fill="var(--gold)">2410 Larkspur Ave NE</text>
      <text class="contact-text" x="265" y="903" fill="var(--gold)">Corvale, Oregon USA 97399</text>

      <g class="contact-icon">
        <circle cx="232" cy="956" r="21" fill="url(#gold-coin)"/>
        <path d="M222,946 l6,-3 l5,9 l-4,3 c2,5 5,8 10,10 l3,-4 l9,5 l-3,6 c-14,0 -26,-12 -26,-26 z" fill="var(--ink)"/>
      </g>
      <text class="contact-text" x="265" y="968" fill="var(--gold)">(555) 014-2837</text>

      <g class="contact-icon">
        <circle cx="232" cy="1052" r="21" fill="url(#gold-coin)"/>
        <rect x="221" y="1045" width="22" height="15" rx="2" fill="none" stroke="var(--ink)" stroke-width="2.5"/>
        <path d="M228,1045 v-4 h8 v4 M221,1051 h22" fill="none" stroke="var(--ink)" stroke-width="2.5"/>
      </g>
      <text class="contact-text" x="265" y="1065" fill="var(--gold)">info@harbingernaw.com</text>

      <g class="contact-icon">
        <circle cx="232" cy="1149" r="21" fill="url(#gold-coin)"/>
        <g fill="none" stroke="var(--ink)" stroke-width="2.2">
          <circle cx="232" cy="1149" r="11"/>
          <ellipse cx="232" cy="1149" rx="5" ry="11"/>
          <path d="M221,1149 h22 M223,1143 h18 M223,1155 h18"/>
        </g>
      </g>
      <text class="contact-text" x="265" y="1162" fill="var(--gold)">https://harbingernaw.com/</text>
    </g>

    <path class="arc arc--gold" d="M106,1463 Q439,1027 773,1463 Z" fill="url(#gold-arc)"/>
    <path class="arc arc--gap" d="M122,1463 Q439,1065 758,1463 Z" fill="var(--ink)"/>
    <path class="arc arc--dome" d="M138,1463 Q439,1129 741,1463 Z" fill="url(#dome-dark)"/>
  </svg>

  <!-- Back -->
  <svg class="card card--back" viewBox="0 0 878 1463" xmlns="http://www.w3.org/2000/svg" aria-label="Business card back with notes area">
    <defs>
      <linearGradient id="back-gold-band" x1="0" y1="0" x2="1" y2="0">
        <stop offset="0" stop-color="#b57a28"/>
        <stop offset="0.5" stop-color="#f1d978"/>
        <stop offset="1" stop-color="#b57a28"/>
      </linearGradient>
      <linearGradient id="back-ring" x1="0" y1="0" x2="0" y2="1">
        <stop offset="0" stop-color="#f3e28a"/>
        <stop offset="1" stop-color="#d9ad3e"/>
      </linearGradient>
      <linearGradient id="back-coin" x1="0" y1="0" x2="0" y2="1">
        <stop offset="0" stop-color="#3a3633"/>
        <stop offset="1" stop-color="#1d1a18"/>
      </linearGradient>
      <linearGradient id="back-dome" x1="0" y1="0" x2="0" y2="1">
        <stop offset="0" stop-color="#f7ec92"/>
        <stop offset="1" stop-color="#c38a34"/>
      </linearGradient>
      <linearGradient id="back-arc" x1="0" y1="0" x2="1" y2="0">
        <stop offset="0" stop-color="#1f1b19"/>
        <stop offset="0.5" stop-color="#3a3633"/>
        <stop offset="1" stop-color="#1f1b19"/>
      </linearGradient>
    </defs>

    <rect class="back-top" width="878" height="1463" fill="var(--ink)"/>
    <path class="wave wave--gold" d="M0,590 C150,520 300,720 438,720 S728,520 878,590 L878,1463 L0,1463 Z" fill="url(#back-gold-band)"/>
    <path class="wave wave--pearl" d="M0,615 C150,550 300,735 438,735 S728,550 878,615 L878,1463 L0,1463 Z" fill="var(--pearl)"/>
    <path class="wave wave--ink" d="M0,640 C150,575 300,760 438,760 S728,575 878,640 L878,1463 L0,1463 Z" fill="var(--ink)"/>
    <path class="wave wave--notes" d="M0,675 C150,610 300,765 438,765 S728,610 878,675 L878,1463 L0,1463 Z" fill="var(--notes)"/>
    <circle class="medallion" cx="438" cy="674" r="47" fill="url(#back-coin)" stroke="url(#back-ring)" stroke-width="12"/>

    <circle class="brand-mark" cx="439" cy="264" r="24" fill="var(--gold)"/>
    <text class="brand-name" x="439" y="352" text-anchor="middle" fill="var(--gold)">Harbinger Noble Alloys Works</text>

    <g class="note-lines" stroke="var(--note-line)" stroke-width="1.6" stroke-dasharray="5 4">
      <line x1="88" y1="853" x2="788" y2="853"/>
      <line x1="88" y1="901" x2="788" y2="901"/>
      <line x1="88" y1="949" x2="788" y2="949"/>
      <line x1="88" y1="998" x2="788" y2="998"/>
      <line x1="88" y1="1046" x2="788" y2="1046"/>
      <line x1="88" y1="1094" x2="788" y2="1094"/>
      <line x1="88" y1="1142" x2="788" y2="1142"/>
    </g>

    <path class="arc arc--ink" d="M93,1463 Q438,983 783,1463 Z" fill="url(#back-arc)"/>
    <path class="arc arc--gap" d="M108,1463 Q438,1040 770,1463 Z" fill="var(--notes)"/>
    <path class="arc arc--dome" d="M123,1463 Q438,1083 755,1463 Z" fill="url(#back-dome)"/>
  </svg>

</main>
</body>
</html>
```